WordPress Site Clean up

We are a small wireless networking company in Norther Colorado. We have a basic layout to our new website, and require a person or persons who can clean the new site up so we can go live with it in the coming weeks. Our company has the logo and content, we just need to clean the formatting up, improve the colors/graphics. It is currently a ZUNPLIKE. We also need help making our project pictures look better on the website, and clean up the images all around.

The website can be found at: www.4qvtelmora.com/newsite

We can provide you with photos and more content, but we have gone as far as we can with "building" the wordpress site.

It Company

```html
<!DOCTYPE html>
<html lang="en">
<head>
<meta charset="utf-8">
<title>Kelvara Networks</title>
<link rel="stylesheet" href="https://fonts.googleapis.com/css2?family=Lato:wght@300;400;700;900&display=swap">
<style>
:root{
  --green:#79a71b;
  --green-dark:#5f8a10;
  --blue:#1f6fc4;
  --blue-light:#3f95e0;
  --ink:#333;
  --muted:#6b6b6b;
  --light:#ececec;
  --grey-band:#545454;
  --footer:#2b2b2b;
  --footer-deep:#1e1e1e;
  --white:#fff;
}
*{box-sizing:border-box;margin:0;padding:0}
html,body{width:1200px;height:3636px;overflow:hidden}
body{font-family:"Lato",Arial,sans-serif;color:var(--ink);background:var(--white);position:relative}
section,header,footer{position:absolute;left:0;width:1200px}
.center{text-align:center}
.accent{color:var(--green);font-weight:700}

/* header */
.site-header{top:0;height:85px;background:#3b3f36;display:flex;align-items:center;padding:0 172px;justify-content:space-between}
.brand{display:flex;align-items:center;gap:12px;color:var(--white);font-size:34px;font-weight:700}
.brand-dot{width:20px;height:20px;border-radius:50%;background:var(--green)}
.header-right{display:flex;flex-direction:column;align-items:flex-end;gap:10px}
.call-pill{background:#1e1e1e;color:#ddd;border-radius:14px;padding:4px 14px;font-size:13px}
.call-pill b{color:var(--white)}
.main-nav{display:flex;gap:24px;font-size:14px;font-weight:900;color:var(--white)}

/* hero */
.hero{top:85px;height:482px;background:linear-gradient(180deg,var(--blue-light),var(--blue))}
.hero h1{position:absolute;left:172px;top:178px;width:500px;color:var(--white);font-size:50px;line-height:52px;font-weight:700}
.hero-photo{position:absolute;left:690px;top:0;width:340px;height:482px;background:linear-gradient(180deg,#5da6e8,#2c7cd0)}
.hero-dots{position:absolute;left:180px;top:450px;display:flex;gap:6px}
.hero-dots span{width:11px;height:11px;border-radius:50%;background:rgba(255,255,255,.55)}
.hero-dots span:first-child{background:var(--white)}

/* welcome */
.welcome{top:567px;height:221px;background:var(--light);padding:40px 172px 0}
.notch{position:absolute;left:576px;top:0;width:0;height:0;border-left:24px solid transparent;border-right:24px solid transparent}
.welcome .notch{border-top:20px solid var(--blue)}
.welcome h2{font-size:34px;font-weight:400;color:#444;margin-bottom:14px}
.welcome p{font-size:19px;line-height:25px;color:#333}

/* services */
.services{top:788px;height:339px;display:flex;justify-content:center;gap:162px;padding-top:55px}
.service{width:135px;text-align:center}
.service-icon{width:135px;height:135px;border:4px solid var(--green);border-radius:50%;display:flex;align-items:center;justify-content:center;margin-bottom:18px}
.service h3{font-size:19px;font-weight:700;margin-bottom:10px}
.service p{width:240px;margin-left:-52px;font-size:12px;line-height:16px;color:var(--muted)}

/* testimonial */
.testimonial{top:1127px;height:140px;background:var(--grey-band);display:flex;align-items:center;padding-left:444px;gap:18px}
.testimonial .notch{border-top:20px solid var(--white)}
.avatar{width:62px;height:62px;border-radius:50%;background:linear-gradient(#c9a78e,#8b6a55);border:3px solid var(--white);flex:none}
.quote{color:var(--white);font-size:13px;line-height:17px;font-style:italic;width:320px}
.quote b{display:block;font-style:normal;margin-top:4px}
.quote small{display:block;font-style:normal;color:#ccc}

/* what we do */
.what{top:1267px;height:773px;background:var(--green);color:var(--white)}
.what h2{padding-top:42px;font-size:32px;font-weight:300}
.what h2 b{font-weight:700}
.what-intro{width:730px;margin:12px auto 0;font-size:13px;line-height:18px}
.gallery{position:absolute;top:142px;left:300px;display:flex;gap:4px}
.gallery div{width:147px;height:131px}
.timeline-line{position:absolute;left:598px;top:300px;width:3px;height:420px;background:var(--white)}
.tl-icon{position:absolute;left:580px;width:40px;height:40px;border-radius:50%;background:var(--white);display:flex;align-items:center;justify-content:center}
.tl-item{position:absolute;width:380px;font-size:12px;line-height:16px}
.tl-item h4{font-size:19px;font-weight:700;margin-bottom:6px}
.tl-right{left:640px}
.tl-left{left:180px;text-align:right}

/* projects */
.projects{top:2040px;height:490px}
.projects h2{padding-top:52px;font-size:32px;font-weight:300;color:#444}
.projects .sub{font-size:13px;color:var(--muted);margin-top:10px}
.cards{position:absolute;top:142px;left:172px;display:flex;gap:12px}
.card{width:210px;height:233px;background:#e8e8e8}
.card-photo{height:130px}
.card h3{font-size:20px;line-height:22px;font-weight:400;padding:12px 14px 4px;color:#222}
.card p{font-size:13px;color:var(--muted);padding:0 14px}
.pager{position:absolute;left:572px;display:flex;gap:6px}
.pager span{width:22px;height:22px;display:flex;align-items:center;justify-content:center;background:var(--white);border:1px solid #ccc}
.pager span.on{background:var(--green);border-color:var(--green)}

/* team */
.team{top:2530px;height:620px;background:#e6e6e6}
.team h2{padding-top:60px;font-size:32px;font-weight:300;color:#444}
.team .sub{width:560px;margin:10px auto 0;font-size:13px;line-height:18px;color:var(--muted)}
.members{position:absolute;top:200px;left:190px;display:flex;gap:12px}
.member{width:212px;height:260px;background:var(--white);border-radius:0 0 60px 60px;text-align:center;position:relative;padding-top:190px}
.member-photo{position:absolute;left:23px;top:-10px;width:166px;height:166px;border-radius:50%;border:5px solid var(--white)}
.member h3{font-size:15px;font-weight:700}
.member .role{font-size:11px;color:var(--muted);margin:2px 0 6px}
.member .bio{font-size:11px;line-height:14px;color:#444;padding:0 20px}

/* partners */
.partners{top:3150px;height:213px}
.partners-rule{position:absolute;top:40px;left:172px;width:856px;height:1px;background:#ccc}
.partners h2{position:absolute;top:28px;left:500px;width:200px;background:var(--white);font-size:14px;letter-spacing:2px;font-weight:400;color:#555}
.partner-row{position:absolute;top:90px;left:172px;width:856px;display:flex;justify-content:space-between;align-items:center}
.badge{height:40px;background:#c4c4c4;border-radius:4px}

/* footer */
.site-footer{top:3363px;height:227px;background:var(--footer);color:var(--white)}
.site-footer h3{font-size:22px;font-weight:700}
.site-footer h3 span{font-weight:300}
.newsletter{position:absolute;left:172px;top:40px}
.signup{display:flex;margin-top:18px}
.signup div{width:340px;height:36px;background:var(--white);color:#999;font-size:12px;padding:10px}
.signup b{width:90px;height:36px;background:var(--green);font-size:13px;display:flex;align-items:center;justify-content:center;font-weight:400}
.helpline{position:absolute;left:660px;top:40px}
.phone{font-size:22px;color:var(--green);margin-top:10px}
.socials{display:flex;gap:10px;margin-top:14px}
.socials span{width:38px;height:38px;border-radius:50%;background:#ddd}
.legal{position:absolute;top:3590px;height:46px;width:1200px;background:var(--footer-deep);color:#aaa;font-size:11px;display:flex;align-items:center;justify-content:center}
</style>
</head>
<body>

<header class="site-header">
  <div class="brand"><span class="brand-dot"></span>Kelvara</div>
  <div class="header-right">
    <div class="call-pill">Call Us Today: <b>1-800-555-0142</b></div>
    <nav class="main-nav"><span>KELVARA ABOUT US</span><span>KELVARA CONTACT US</span><span>KELVARA BLOG</span></nav>
  </div>
</header>

<section class="hero">
  <h1>All Your Wireless Needs A Professional Solution</h1>
  <div class="hero-photo" role="img" aria-label="Photo of a cellular antenna tower against a blue sky"></div>
  <div class="hero-dots"><span></span><span></span><span></span><span></span><span></span></div>
</section>

<section class="welcome">
  <div class="notch"></div>
  <h2>Welcome to <span class="accent">Kelvara Networks</span></h2>
  <p>Lorem ipsum dolor sit amet, consectetur adipiscing elit, sed do eiusmod tempor incididunt ut labore et dolore magna aliqua. Ut enim ad minim veniam, quis nostrud exercitation ullamco laboris nisi ut aliquip ex ea commodo consequat.</p>
</section>

<section class="services">
  <div class="service">
    <div class="service-icon">
      <svg width="60" height="60" viewBox="0 0 60 60"><g fill="#222"><circle cx="24" cy="34" r="14"/><circle cx="44" cy="18" r="10"/></g><g fill="#fff"><circle cx="24" cy="34" r="5"/><circle cx="44" cy="18" r="3.5"/></g></svg>
    </div>
    <h3>Services</h3>
    <p>Providing world class services is Kelvara Network's commitment. We provide a whole host of services from installation to design work.</p>
  </div>
  <div class="service">
    <div class="service-icon">
      <svg width="60" height="60" viewBox="0 0 60 60" fill="none" stroke="#222" stroke-width="4"><circle cx="28" cy="30" r="20"/><circle cx="28" cy="30" r="9"/><path d="M32 34l18 18"/></svg>
    </div>
    <h3>Solutions</h3>
    <p>Providing world class services is Kelvara Network's commitment. We provide a whole host of services from installation to design work.</p>
  </div>
  <div class="service">
    <div class="service-icon">
      <svg width="60" height="60" viewBox="0 0 60 60" fill="none" stroke="#222" stroke-width="4"><circle cx="30" cy="30" r="20"/><path d="M18 42l24-24M36 14l10 10"/></svg>
    </div>
    <h3>Design</h3>
    <p>Providing world class services is Kelvara Network's commitment. We provide a whole host of services from installation to design work.</p>
  </div>
</section>

<section class="testimonial">
  <div class="notch"></div>
  <div class="avatar" role="img" aria-label="Portrait of the client giving the testimonial"></div>
  <p class="quote">Lorem ipsum dolor sit amet, consectetur adipiscing elit, sed do eiusmod tempor incididunt ut labore et dolore magna aliqua.<b>Anna R.</b><small>Lorem ipsum</small></p>
</section>

<section class="what">
  <h2 class="center">What <b>We Do</b></h2>
  <p class="what-intro center">We live in a digital world that is connected. We are here to make those connections, and help our customers succeed. Whatever your IT need or goal is, we will strive to meet and exceed your expectations.</p>
  <div class="gallery">
    <div role="img" aria-label="Photo of a network equipment cabinet" style="background:linear-gradient(#d9d9d9,#8a8a8a)"></div>
    <div role="img" aria-label="Photo of a server rack with cabling" style="background:linear-gradient(#5f6f7a,#2a3238)"></div>
    <div role="img" aria-label="Wireless coverage heat map" style="background:linear-gradient(135deg,#e9eef2,#7cc9e8 50%,#e06a4a)"></div>
    <div role="img" aria-label="Photo of a technician at a network rack" style="background:linear-gradient(#6c625a,#2f2a26)"></div>
  </div>
  <div class="timeline-line"></div>

  <div class="tl-icon" style="top:315px"><svg width="20" height="20" viewBox="0 0 20 20"><circle cx="10" cy="10" r="8" fill="none" stroke="#333" stroke-width="2"/><circle cx="10" cy="10" r="3" fill="#333"/></svg></div>
  <div class="tl-item tl-right" style="top:306px"><h4>Our Solutions</h4>We provide consulting, design, regulatory knowledge, installation, repair, tower climbing, data/voice/video cabling, wireless networking, switches, routers, project management and complete managed services.</div>

  <div class="tl-icon" style="top:390px"><svg width="20" height="20" viewBox="0 0 20 20" fill="#333"><circle cx="10" cy="6" r="4"/><path d="M2 19c0-5 4-7 8-7s8 2 8 7z"/></svg></div>
  <div class="tl-item tl-left" style="top:377px"><h4>Customer Focus</h4>The Customer is Kelvara Network's primary focus. We strive for 100% Customer Satisfaction in every aspect of the job. We will provide the best solution at the best price with no short cuts.</div>

  <div class="tl-icon" style="top:470px"><svg width="20" height="20" viewBox="0 0 20 20" fill="none" stroke="#333" stroke-width="2"><path d="M10 2l7 3v5c0 4-3 7-7 8-4-1-7-4-7-8V5z"/><path d="M7 10l2 2 4-4"/></svg></div>
  <div class="tl-item tl-right" style="top:457px"><h4>Safety First</h4>Kelvara Networks makes safety priority one for both the customer and its employees. Kelvara Networks stays current on the latest industry standards and receives them in providing services and products.</div>

  <div class="tl-icon" style="top:548px"><svg width="20" height="20" viewBox="0 0 20 20" fill="none" stroke="#333" stroke-width="2"><rect x="3" y="6" width="14" height="11" rx="1"/><path d="M7 6V3h6v3"/></svg></div>
  <div class="tl-item tl-left" style="top:535px"><h4>Professionalism</h4>Anyone doing business with Kelvara Networks will come to expect the up most professionalism. All employees within Kelvara Networks will be treated with professionalism and in return will be expected to do a professional job each day.</div>

  <div class="tl-icon" style="top:628px"><svg width="20" height="20" viewBox="0 0 20 20" fill="none" stroke="#333" stroke-width="2"><circle cx="10" cy="8" r="5"/><path d="M7 12l-2 6 5-2 5 2-2-6"/></svg></div>
  <div class="tl-item tl-right" style="top:615px"><h4>Quality</h4>Kelvara Networks will never substitute or sacrifice quality in providing products and services to any of its customers, and will continually seek out the best in terms of industry products, procedures and solutions.</div>
</section>

<section class="projects">
  <h2 class="center">Our Latest <span class="accent">Projects</span></h2>
  <p class="sub center">Take a look at our latest projects and learn more about what we can do for you and your networking needs.</p>
  <div class="cards">
    <article class="card"><div class="card-photo" role="img" aria-label="Photo of a rooftop wireless installation" style="background:linear-gradient(#d6e3ee,#8e8e8e)"></div><h3>Wireless Solution Lumber Yard</h3><p>Indoor Wireless</p></article>
    <article class="card"><div class="card-photo" role="img" aria-label="Photo of a point-to-point radio on a rooftop" style="background:linear-gradient(#b8cfe3,#b48a63)"></div><h3>Linkpeak LP80 / Ardent PTP 600</h3><p>Point-to-Point</p></article>
    <article class="card"><div class="card-photo" role="img" aria-label="Photo of twin radio links on a roof mast" style="background:linear-gradient(#c7d7e6,#a9876a)"></div><h3>Dual Linkpeak LP80 Links</h3><p>Point-to-Point</p></article>
    <article class="card"><div class="card-photo" role="img" aria-label="Photo of structured cabling in a school" style="background:linear-gradient(#8a8f94,#3b3f44)"></div><h3>Charter School Cabling</h3><p>Data Cabling</p></article>
  </div>
  <div class="pager" style="top:407px">
    <span><svg width="8" height="10" viewBox="0 0 8 10"><path d="M6 1L2 5l4 4" stroke="#888" stroke-width="2" fill="none"/></svg></span>
    <span class="on"><svg width="8" height="10" viewBox="0 0 8 10"><path d="M2 1l4 4-4 4" stroke="#fff" stroke-width="2" fill="none"/></svg></span>
  </div>
</section>

<section class="team">
  <h2 class="center">Meet Our <span class="accent">Amazing Team</span></h2>
  <p class="sub center">Experience is what drives our team. With our combination of experience and knowledge, we can solve your problems and provide you with knowledge to help you make decisions.</p>
  <div class="members">
    <div class="member"><div class="member-photo" role="img" aria-label="Portrait of Mark Ellison" style="background:linear-gradient(#6b6b6b,#3a3a3a)"></div><h3>Mark Ellison</h3><p class="role">CEO, Founder</p><p class="bio">Mark Ellison has 24+ years of experience in the data/networking industry.</p></div>
    <div class="member"><div class="member-photo" role="img" aria-label="Portrait of Dean Ellison" style="background:linear-gradient(#5e7f9a,#2e4458)"></div><h3>Dean Ellison</h3><p class="role">VP of Sales and Marketing</p><p class="bio">Dean Ellison has 12+ years experience in sales in wireless networking.</p></div>
    <div class="member"><div class="member-photo" role="img" aria-label="Portrait of Paul Ridley" style="background:linear-gradient(#8a8f94,#4b5056)"></div><h3>Paul Ridley</h3><p class="role">Sales Executive</p><p class="bio">Paul Ridley has 30+ years experience in sales and customer service.</p></div>
    <div class="member"><div class="member-photo" role="img" aria-label="Portrait of RT Coleman" style="background:linear-gradient(#b9c1c8,#6f7a84)"></div><h3>RT Coleman</h3><p class="role">Systems Engineer</p><p class="bio">RT has 5+ years experience to develop support and network engineering.</p></div>
  </div>
  <div class="pager" style="top:490px">
    <span><svg width="8" height="10" viewBox="0 0 8 10"><path d="M6 1L2 5l4 4" stroke="#888" stroke-width="2" fill="none"/></svg></span>
    <span class="on"><svg width="8" height="10" viewBox="0 0 8 10"><path d="M2 1l4 4-4 4" stroke="#fff" stroke-width="2" fill="none"/></svg></span>
  </div>
</section>

<section class="partners">
  <div class="partners-rule"></div>
  <h2 class="center">OUR PARTNERS</h2>
  <div class="partner-row">
    <div class="badge" style="width:110px"></div>
    <div class="badge" style="width:130px"></div>
    <div class="badge" style="width:120px"></div>
    <div class="badge" style="width:115px"></div>
    <div class="badge" style="width:140px"></div>
    <div class="badge" style="width:120px"></div>
  </div>
</section>

<footer class="site-footer">
  <div class="newsletter">
    <h3>News<span>letter</span></h3>
    <div class="signup"><div>Stay up to date with our latest news</div><b>Subscribe</b></div>
  </div>
  <div class="helpline">
    <h3>Help<span>Line</span></h3>
    <p class="phone">
      <svg width="16" height="16" viewBox="0 0 16 16" fill="#79a71b"><path d="M3 1l3 3-2 2c1 2 3 4 5 5l2-2 3 3-2 3C7 15 1 9 0 3z"/></svg>
      +44(0) 100 555 0199
    </p>
    <div class="socials"><span></span><span></span><span></span></div>
  </div>
</footer>
<div class="legal">© 2015 Kelvara Networks. All Rights Reserved &nbsp;•&nbsp; Terms and Conditions &nbsp;•&nbsp; Privacy Policy &nbsp;•&nbsp; Terms of Use</div>

</body>
</html>
```